Harrowfield Security Solutions Trade Show

Backdrop for trade show and table cover. Colors to use are red, black and silver/grey . Logo attached. If you are able to view the website and pull any images, that would be great. Website is https://harrowfieldsecuritywx.com/

```html
<!DOCTYPE html>
<html lang="en">
<head>
<meta charset="utf-8">
<title>Harrowfield Security Solutions – Trade Show Backdrop</title>
<link rel="stylesheet" href="https://fonts.googleapis.com/css2?family=Archivo+Black&display=swap">
<style>
  :root {
    --stage: #d9d4bf;
    --signal-red: #ec4a24;
    --deep-red: #c2321a;
    --panel-white: #ffffff;
    --ink-navy: #1f2634;
    --photo-light: #8b9096;
    --photo-mid: #4d545c;
    --photo-dark: #23272d;
  }
  html, body {
    margin: 0;
    width: 1200px;
    height: 1200px;
    overflow: hidden;
    background: var(--stage);
  }
  .backdrop {
    position: absolute;
    left: 80px;
    top: 100px;
    width: 1040px;
    height: 1000px;
  }
  .backdrop svg { display: block; }
  .headline {
    font-family: "Archivo Black", sans-serif;
    text-anchor: end;
  }
  .headline-solid { fill: var(--panel-white); }
  .headline-outline {
    fill: none;
    stroke: var(--panel-white);
    stroke-width: 2.5;
  }
  .brand-name {
    font-family: "Archivo Black", sans-serif;
    fill: var(--ink-navy);
    text-anchor: middle;
  }
</style>
</head>
<body>
  <div class="backdrop">
    <svg width="1040" height="1000" viewBox="0 0 1040 1000" xmlns="http://www.w3.org/2000/svg">
      <defs>
        <linearGradient id="photoTone" x1="0" y1="0" x2="1" y2="1">
          <stop offset="0" stop-color="var(--photo-light)"/>
          <stop offset="0.45" stop-color="var(--photo-mid)"/>
          <stop offset="1" stop-color="var(--photo-dark)"/>
        </linearGradient>
        <linearGradient id="redEdge" x1="0" y1="0" x2="1" y2="0">
          <stop offset="0" stop-color="var(--deep-red)"/>
          <stop offset="0.12" stop-color="var(--signal-red)"/>
          <stop offset="0.9" stop-color="var(--signal-red)"/>
          <stop offset="1" stop-color="var(--deep-red)"/>
        </linearGradient>
      </defs>

      <rect class="photo-area" x="0" y="0" width="1040" height="1000" fill="url(#photoTone)"
            role="img" aria-label="Photo of a uniformed security officer seated at the wheel of a dark patrol vehicle"/>

      <polygon class="top-band" points="0,0 660,0 539,195 0,30" fill="var(--signal-red)"/>

      <polygon class="brand-panel" points="660,0 1040,0 1040,75 829,394 415,394" fill="var(--panel-white)"/>

      <polygon class="message-field" points="1040,75 1040,1000 0,1000 0,870 395,870 700,394 829,394" fill="url(#redEdge)"/>

      <text class="brand-name" x="735" y="250" font-size="40">HARROWFIELD</text>
      <text class="brand-name" x="735" y="285" font-size="17" letter-spacing="3.5">SECURITY SOLUTIONS</text>

      <text class="headline headline-solid" x="962" y="603" font-size="76">EXCEPTIONAL</text>
      <text class="headline headline-outline" x="962" y="713" font-size="104">SECURITY</text>
      <text class="headline headline-outline" x="962" y="825" font-size="104">GUARD</text>
      <text class="headline headline-solid" x="962" y="915" font-size="78">SOLUTIONS</text>
    </svg>
  </div>
</body>
</html>
```